Velvet corsaro

I want a business card design. the company is an infrastructure development company.

Target Market(s)

Government
real estate investors
real estate clients

Industry/Entity Type

Business

```html
<!DOCTYPE html>
<html lang="en">
<head>
<meta charset="utf-8">
<title>Velvet Corsaro – Business Card</title>
<link rel="stylesheet" href="https://fonts.googleapis.com/css2?family=Crimson+Pro:wght@400;600;700&family=Marcellus&display=swap">
<style>
  :root {
    --stage: #333233;
    --paper: #ffffff;
    --brand-red: #e1333c;
    --brand-red-deep: #cf2f37;
    --brand-blue: #00aeef;
    --rule-blue: #1f6fd6;
    --tagline-grey: #8c8c8c;
    --ink-light: #ffffff;
    --body-font: "Crimson Pro", Georgia, serif;
    --tag-font: "Marcellus", Georgia, serif;
  }
  * { margin: 0; padding: 0; box-sizing: border-box; }
  html, body { width: 938px; height: 1200px; overflow: hidden; }
  body { background: var(--stage); position: relative; font-family: var(--body-font); }

  .card { position: absolute; background: var(--paper); overflow: hidden; }
  .card--back  { left: 53px; top: 58px;  width: 832px; height: 508px; }
  .card--front { left: 61px; top: 611px; width: 816px; height: 498px; }

  .brand {
    position: absolute; left: 0; right: 0;
    display: flex; align-items: center; justify-content: center; gap: 16px;
    color: var(--brand-red); font-weight: 600; text-transform: uppercase;
    letter-spacing: 0.04em; line-height: 1;
  }
  .brand__mark { background: var(--brand-blue); flex: none; }
  .card--back .brand { top: 62px; font-size: 50px; }
  .card--back .brand__mark { width: 30px; height: 30px; }
  .card--front .brand { top: 160px; font-size: 72px; gap: 22px; }
  .card--front .brand__mark { width: 44px; height: 44px; }

  .tagline {
    position: absolute; left: 0; right: 0; text-align: center;
    font-family: var(--tag-font); color: var(--tagline-grey); letter-spacing: 0.03em;
  }
  .card--back .tagline { top: 174px; font-size: 22px; }
  .card--front .tagline { top: 364px; font-size: 29px; }

  .rule { position: absolute; left: 0; right: 0; top: 216px; height: 6px; background: var(--rule-blue); }

  .band {
    position: absolute; left: 0; right: 0; bottom: 0;
    background: linear-gradient(100deg, var(--brand-red) 0%, var(--brand-red) 45%, var(--brand-red-deep) 100%);
    color: var(--ink-light);
  }
  .card--back .band { top: 222px; }
  .card--front .band { height: 63px; }

  .website {
    position: absolute; left: 0; right: 0; text-align: center;
    font-size: 22px; letter-spacing: 0.08em;
  }
  .card--back .website { bottom: 8px; }
  .card--front .website { top: 15px; }

  .contact { position: absolute; top: 0; font-size: 17px; line-height: 1; }
  .contact--person { left: 133px; }
  .contact--office { left: 466px; }
  .divider { position: absolute; left: 433px; top: 10px; width: 1px; height: 212px; background: rgba(255,255,255,0.8); }

  .contact__name { position: absolute; top: 18px; white-space: nowrap; font-size: 27px; font-weight: 700; }
  .contact__role { position: absolute; top: 60px; white-space: nowrap; font-size: 17px; }
  .contact__company { position: absolute; top: 22px; white-space: nowrap; font-size: 19px; font-weight: 700; }
  .contact__address { position: absolute; top: 52px; white-space: nowrap; font-size: 17px; font-weight: 600; line-height: 31px; }
  .contact__lines { position: absolute; top: 118px; list-style: none; white-space: nowrap; font-size: 17px; line-height: 30px; }
  .contact--office .contact__lines { font-weight: 600; }
</style>
</head>
<body>

  <section class="card card--back" aria-label="Business card, reverse side">
    <div class="brand"><span class="brand__mark"></span><span>Velvet Corsaro</span></div>
    <p class="tagline">Infrastructure Development</p>
    <div class="rule"></div>
    <div class="band">
      <div class="contact contact--person">
        <p class="contact__name">Adaeze Okonkwo</p>
        <p class="contact__role">Managing Director</p>
        <ul class="contact__lines">
          <li>Ph: +234 8051427730</li>
          <li>Ph: +234 7082615904</li>
          <li>Mail: aokonkwo@velvetcorsaro.com</li>
        </ul>
      </div>
      <div class="divider"></div>
      <div class="contact contact--office">
        <p class="contact__company">Velvet Corsaro</p>
        <p class="contact__address">12, Marula Close, Off Harbour View Road,<br>Ikoyi Lagos, Nigeria</p>
        <ul class="contact__lines">
          <li>Ph: +234 14527719</li>
          <li>Ph: +234 7093148256</li>
          <li>Mail:&nbsp; info@velvetcorsaro.com</li>
        </ul>
      </div>
      <p class="website">www.velvetcorsaro.com</p>
    </div>
  </section>

  <section class="card card--front" aria-label="Business card, front side">
    <div class="brand"><span class="brand__mark"></span><span>Velvet Corsaro</span></div>
    <p class="tagline">Infrastructure Development</p>
    <div class="band">
      <p class="website">www.velvetcorsaro.com</p>
    </div>
  </section>

</body>
</html>
```